Sales Deck Redesign for a B2B business selling customer service AI products

We are looking for a redesign of our sales Deck. we are a B2B business selling customer service AI products.

The sales deck is attached, we would like this to be made less "powerpoint" and more "professional expertise in a friendly package".

Our brand standards are attached with details on logos, colours and imagery.

Other examples of inspiration:
-Our website: https://www.brevora.example/
-Cloudvane imagery - we are a Cloudvane partner, so linking imagery with Cloudvane would help.
-Competitor: https://www.tellimo.example/
-Brevora Scorecard landing page: https://brevora.quizpage.example/

Full image files and AI/PNG files available on request

Slide 17 is a very rough design but if you can create something that is in line with the rest of the deck that would be great

Target Market(s)

Customer service teams and contact centres

Industry/Entity Type

Technology - Cloudvane Ecosystem

Colors
0054AA
0677BA
7BADD7
CADEEF
E8F1F8

Requirements
Must have
• See description and branding doc
Nice to have
Should not have

```html
<!DOCTYPE html>
<html lang="en">
<head>
<meta charset="utf-8">
<title>Brevora AI – Sales Deck</title>
<link href="https://fonts.googleapis.com/css2?family=Inter:wght@400;500;600;700;800&display=swap" rel="stylesheet">
<style>
:root{
  --page:#7b7b7b;
  --navy:#0b1530;
  --deep:#2a236f;
  --orange:#f5821f;
  --blue:#0a8fd6;
  --blue-dark:#0054aa;
  --blue-mid:#0677ba;
  --blue-soft:#7badd7;
  --blue-pale:#cadeef;
  --blue-mist:#e8f1f8;
  --ink:#111827;
  --grey:#6b6f78;
  --white:#ffffff;
}
*{box-sizing:border-box;margin:0;padding:0}
html,body{width:1200px;height:4351px;overflow:hidden}
body{background:var(--page);font-family:"Inter",Arial,sans-serif;color:var(--ink);position:relative}
.slide{position:absolute;left:24px;width:1151px;height:647px;background:var(--white);overflow:hidden;box-shadow:0 2px 8px rgba(0,0,0,.25)}
.brand{position:absolute;display:flex;align-items:center;gap:10px;font-weight:600;letter-spacing:4px;font-size:22px;color:var(--blue-dark)}
.brand .dot{width:30px;height:30px;border-radius:50%;border:3px solid currentColor}
.slide-head .brand{right:30px;top:50px}
.slide-title{position:absolute;left:58px;top:60px;font-size:29px;font-weight:700;color:var(--ink)}
.rule{position:absolute;left:0;right:0;top:124px;height:1px;background:var(--blue-pale)}
.rule-accent{position:absolute;left:58px;top:121px;width:50px;height:6px;border-radius:3px;background:var(--blue)}
.footer{position:absolute;left:0;right:0;bottom:0;height:44px;background:var(--deep);display:flex;align-items:center;font-size:10px;color:var(--white)}
.footer .copy{padding-left:58px;flex:1}
.footer .copy a{color:var(--blue-soft);text-decoration:underline}
.footer .page{width:193px;height:100%;background:var(--orange);display:flex;align-items:center;justify-content:center}
.art{position:absolute;border-radius:40% 40% 30% 30%}
.art-robot{background:radial-gradient(ellipse at 50% 40%,#5fc3f3 0%,#1a8ee0 45%,#0d5fb0 75%,rgba(13,95,176,0) 76%)}

/* cover */
.cover{top:37px;height:648px;background:var(--navy)}
.cover .photo{position:absolute;right:0;top:0;width:700px;height:100%;background:linear-gradient(90deg,var(--navy) 0%,#2a2c38 25%,#5a5149 60%,#8a7560 100%)}
.cover .brand{left:54px;top:190px;color:var(--white);font-size:26px}
.cover h1{position:absolute;left:54px;top:280px;font-size:44px;line-height:56px;font-weight:800;color:var(--white)}
.cover p{position:absolute;left:54px;top:410px;font-size:16px;line-height:27px;color:var(--white)}

/* problems */
.problems{top:749px}
.problem{position:absolute;display:flex;align-items:center;gap:22px;width:440px}
.problem .x{flex:none;width:66px;height:66px;border-radius:50%;background:var(--blue);display:flex;align-items:center;justify-content:center}
.problem p{font-size:11px;line-height:20px;color:var(--grey)}

/* process */
.process{top:1470px}
.card{position:absolute;left:57px;width:240px;height:85px;background:var(--white);border-radius:10px;box-shadow:0 3px 14px rgba(0,40,90,.13);display:flex;align-items:center;gap:20px;padding-left:22px;font-size:16px;font-weight:600;line-height:26px}
.feature{position:absolute;left:334px;font-size:11px;color:#333;white-space:nowrap;display:flex;align-items:center}
.feature b{font-size:14px;color:var(--ink);margin-right:10px;font-weight:700}
.tick{flex:none;width:13px;height:13px;margin-right:14px}

/* chatbot */
.chatbot{top:2192px}
.lead{position:absolute;left:58px;font-size:13px;line-height:24px;color:#333}
.point{position:absolute;left:58px;display:flex;align-items:center;font-size:14px;font-weight:600}
.source{position:absolute;left:58px;top:559px;font-size:11px;color:#333}
.beta{top:2919px}
.sub{position:absolute;left:86px;font-size:12px;line-height:23px;color:#333}

/* closing */
.closing{top:3639px;background:radial-gradient(ellipse at 78% 45%,#1c7bbf 0%,#0d3f78 35%,#061a3a 75%)}
.closing .brand{left:82px;top:203px;color:var(--white);font-size:28px}
.closing h2{position:absolute;left:82px;top:334px;font-size:62px;font-weight:800;color:var(--white)}
.closing .site{position:absolute;left:100px;top:436px;display:flex;align-items:center;gap:14px;color:var(--white);font-size:15px;letter-spacing:2px}
.closing .follow{position:absolute;left:82px;top:498px;display:flex;align-items:center;gap:8px;color:var(--white);font-size:20px;font-weight:600}
.closing .follow i{width:28px;height:28px;border-radius:50%;background:var(--blue);display:inline-block}
</style>
</head>
<body>

<section class="slide cover">
  <div class="photo" role="img" aria-label="Photo of two colleagues reviewing a laptop in a server room"></div>
  <div class="brand"><span class="dot"></span>BREVORA AI</div>
  <h1>Automated Quality<br>Assurance A.I.</h1>
  <p>Automate your Quality Assurance and improve<br>your insight by 50x</p>
</section>

<section class="slide problems slide-head">
  <h2 class="slide-title">Manual QA Lacks Insight &amp; Wastes Resources</h2>
  <div class="brand"><span class="dot"></span>BREVORA AI</div>
  <div class="rule"></div><div class="rule-accent"></div>
  <div class="problem" style="left:85px;top:183px"><span class="x"><svg width="22" height="22" viewBox="0 0 22 22"><path d="M4 4L18 18M18 4L4 18" stroke="#fff" stroke-width="4" stroke-linecap="round"/></svg></span><p>On average, only 2% of all cases will be audited</p></div>
  <div class="problem" style="left:85px;top:297px"><span class="x"><svg width="22" height="22" viewBox="0 0 22 22"><path d="M4 4L18 18M18 4L4 18" stroke="#fff" stroke-width="4" stroke-linecap="round"/></svg></span><p>Cases are randomly selected, meaning issues can be missed</p></div>
  <div class="problem" style="left:85px;top:410px"><span class="x"><svg width="22" height="22" viewBox="0 0 22 22"><path d="M4 4L18 18M18 4L4 18" stroke="#fff" stroke-width="4" stroke-linecap="round"/></svg></span><p>Compliance and soft skill risks are only found on randomly<br>selected cases, not the other 98%</p></div>
  <div class="problem" style="left:602px;top:183px"><span class="x"><svg width="22" height="22" viewBox="0 0 22 22"><path d="M4 4L18 18M18 4L4 18" stroke="#fff" stroke-width="4" stroke-linecap="round"/></svg></span><p>QA tools are not integrated, or worse... on spreadsheets!</p></div>
  <div class="problem" style="left:602px;top:297px"><span class="x"><svg width="22" height="22" viewBox="0 0 22 22"><path d="M4 4L18 18M18 4L4 18" stroke="#fff" stroke-width="4" stroke-linecap="round"/></svg></span><p>Reporting is delayed, with no key reporting/dashboards</p></div>
  <div class="problem" style="left:602px;top:410px"><span class="x"><svg width="22" height="22" viewBox="0 0 22 22"><path d="M4 4L18 18M18 4L4 18" stroke="#fff" stroke-width="4" stroke-linecap="round"/></svg></span><p>Feedback training cycles are slow and lack impact</p></div>
  <div class="footer"><span class="copy">(C) Copyright 2024 <a>Brevora</a> | All Rights Reserved</span><span class="page">Page 02</span></div>
</section>

<section class="slide process slide-head">
  <h2 class="slide-title">Process AI</h2>
  <div class="brand"><span class="dot"></span>BREVORA AI</div>
  <div class="rule"></div><div class="rule-accent"></div>
  <div class="card" style="top:186px"><svg width="34" height="30" viewBox="0 0 34 30" fill="none" stroke="#0a8fd6" stroke-width="1.6"><rect x="3" y="12" width="22" height="14" rx="2"/><path d="M8 17h12M8 21h8"/><circle cx="27" cy="7" r="4"/></svg>Bespoke Chatbots</div>
  <div class="card" style="top:314px"><svg width="34" height="30" viewBox="0 0 34 30" fill="none" stroke="#0a8fd6" stroke-width="1.6"><rect x="3" y="12" width="22" height="14" rx="2"/><path d="M8 17h12M8 21h8"/><circle cx="27" cy="7" r="4"/></svg>AI-Assisted<br>Case Handling</div>
  <div class="card" style="top:442px"><svg width="34" height="30" viewBox="0 0 34 30" fill="none" stroke="#0a8fd6" stroke-width="1.6"><rect x="3" y="12" width="22" height="14" rx="2"/><path d="M8 17h12M8 21h8"/><circle cx="27" cy="7" r="4"/></svg>Measure your<br>Impact on Service</div>
  <div class="feature" style="top:196px"><svg class="tick" viewBox="0 0 13 13"><circle cx="6.5" cy="6.5" r="6.5" fill="#f5821f"/><path d="M3.5 6.8l2 2 4-4" stroke="#fff" stroke-width="1.6" fill="none"/></svg><b>Automated Case Categorisation</b>Get cases to the right team the first time, reducing human error &amp; cost-to-serve</div>
  <div class="feature" style="top:239px"><svg class="tick" viewBox="0 0 13 13"><circle cx="6.5" cy="6.5" r="6.5" fill="#f5821f"/><path d="M3.5 6.8l2 2 4-4" stroke="#fff" stroke-width="1.6" fill="none"/></svg><b>Intelligent Knowledge Base Recommendations</b>Provide customers with relevant recommendations based on their requests.</div>
  <div class="feature" style="top:282px"><svg class="tick" viewBox="0 0 13 13"><circle cx="6.5" cy="6.5" r="6.5" fill="#f5821f"/><path d="M3.5 6.8l2 2 4-4" stroke="#fff" stroke-width="1.6" fill="none"/></svg><b>Proactive Next Best Action Identification</b>Determine the most suitable next steps for agents to enhance customer experiences.</div>
  <div class="feature" style="top:325px"><svg class="tick" viewBox="0 0 13 13"><circle cx="6.5" cy="6.5" r="6.5" fill="#f5821f"/><path d="M3.5 6.8l2 2 4-4" stroke="#fff" stroke-width="1.6" fill="none"/></svg><b>Emotion Analysis for Chatbot Interactions</b>Analyse customer emotions in response to your chatbot interactions</div>
  <div class="feature" style="top:368px"><svg class="tick" viewBox="0 0 13 13"><circle cx="6.5" cy="6.5" r="6.5" fill="#f5821f"/><path d="M3.5 6.8l2 2 4-4" stroke="#fff" stroke-width="1.6" fill="none"/></svg><b>Streamlined Case Efficiency Tracking</b>Monitor and optimise case handling efficiency by process for improved customer experience</div>
  <div class="feature" style="top:411px"><svg class="tick" viewBox="0 0 13 13"><circle cx="6.5" cy="6.5" r="6.5" fill="#f5821f"/><path d="M3.5 6.8l2 2 4-4" stroke="#fff" stroke-width="1.6" fill="none"/></svg><b>Chatbot Impact Analysis</b>Understand how your chatbot influences overall customer satisfaction.</div>
  <div class="art art-robot" style="left:940px;top:400px;width:115px;height:180px" role="img" aria-label="Illustration of a friendly blue robot mascot"></div>
  <div class="footer"><span class="copy">(C) Copyright 2024 <a>Brevora</a> | All Rights Reserved</span><span class="page">Page 03</span></div>
</section>

<section class="slide chatbot slide-head">
  <h2 class="slide-title">Bespoke AI Chatbot</h2>
  <div class="brand"><span class="dot"></span>BREVORA AI</div>
  <div class="rule"></div><div class="rule-accent"></div>
  <p class="lead" style="top:164px">On average, live chat and chatbots handle 69% of all contact centre conversations. On top of this, 31% of<br>customer service organizations plan to start using chatbots within the next 18 months.<br>Stay ahead of the curve with chatbots that understand your products/services and customers’ requests.</p>
  <div class="point" style="top:268px"><svg class="tick" viewBox="0 0 13 13"><circle cx="6.5" cy="6.5" r="6.5" fill="#f5821f"/><path d="M3.5 6.8l2 2 4-4" stroke="#fff" stroke-width="1.6" fill="none"/></svg>Trained on your knowledge base for accurate support</div>
  <div class="point" style="top:311px"><svg class="tick" viewBox="0 0 13 13"><circle cx="6.5" cy="6.5" r="6.5" fill="#f5821f"/><path d="M3.5 6.8l2 2 4-4" stroke="#fff" stroke-width="1.6" fill="none"/></svg>Elevate your self-serve offering</div>
  <div class="point" style="top:354px"><svg class="tick" viewBox="0 0 13 13"><circle cx="6.5" cy="6.5" r="6.5" fill="#f5821f"/><path d="M3.5 6.8l2 2 4-4" stroke="#fff" stroke-width="1.6" fill="none"/></svg>Reduce wait times &amp; cost-to-serve</div>
  <div class="point" style="top:397px"><svg class="tick" viewBox="0 0 13 13"><circle cx="6.5" cy="6.5" r="6.5" fill="#f5821f"/><path d="M3.5 6.8l2 2 4-4" stroke="#fff" stroke-width="1.6" fill="none"/></svg>Agents can focus on complex cases</div>
  <div class="point" style="top:440px"><svg class="tick" viewBox="0 0 13 13"><circle cx="6.5" cy="6.5" r="6.5" fill="#f5821f"/><path d="M3.5 6.8l2 2 4-4" stroke="#fff" stroke-width="1.6" fill="none"/></svg>Integrate with Cloudvane and sites/portals</div>
  <div class="point" style="top:483px"><svg class="tick" viewBox="0 0 13 13"><circle cx="6.5" cy="6.5" r="6.5" fill="#f5821f"/><path d="M3.5 6.8l2 2 4-4" stroke="#fff" stroke-width="1.6" fill="none"/></svg>Increase CSAT &amp; NPS scores Expected H1 2024</div>
  <p class="source">Source: Cloudvane &amp; Chatmetric</p>
  <div class="art art-robot" style="left:720px;top:166px;width:253px;height:414px" role="img" aria-label="Illustration of a smiling blue robot mascot with arms raised"></div>
  <div class="footer"><span class="copy">(C) Copyright 2024 <a>Brevora</a> | All Rights Reserved</span><span class="page">Page 04</span></div>
</section>

<section class="slide beta slide-head">
  <h2 class="slide-title">Quality AI Beta Program</h2>
  <div class="brand"><span class="dot"></span>BREVORA AI</div>
  <div class="rule"></div><div class="rule-accent"></div>
  <p class="lead" style="top:206px">Working with our existing clients to improve product offering and sharing the experience to grow<br>the Brevora Family</p>
  <div class="point" style="top:311px"><svg class="tick" viewBox="0 0 13 13"><circle cx="6.5" cy="6.5" r="6.5" fill="#f5821f"/><path d="M3.5 6.8l2 2 4-4" stroke="#fff" stroke-width="1.6" fill="none"/></svg>1-year of free access to upgraded Quality AI</div>
  <div class="point" style="top:354px"><svg class="tick" viewBox="0 0 13 13"><circle cx="6.5" cy="6.5" r="6.5" fill="#f5821f"/><path d="M3.5 6.8l2 2 4-4" stroke="#fff" stroke-width="1.6" fill="none"/></svg>Premium Support included</div>
  <div class="point" style="top:397px"><svg class="tick" viewBox="0 0 13 13"><circle cx="6.5" cy="6.5" r="6.5" fill="#f5821f"/><path d="M3.5 6.8l2 2 4-4" stroke="#fff" stroke-width="1.6" fill="none"/></svg>Early access to</div>
  <p class="sub" style="top:435px">Knowledge Base Assistance<br>Bespoke AI Chatbot</p>
  <div class="art art-robot" style="left:700px;top:150px;width:290px;height:410px" role="img" aria-label="Illustration of a smiling blue robot mascot with hands on hips"></div>
  <div class="footer"><span class="copy">(C) Copyright 2024 <a>Brevora</a> | All Rights Reserved</span><span class="page">Page 05</span></div>
</section>

<section class="slide closing" role="img" aria-label="Abstract blue digital network background">
  <div class="brand"><span class="dot"></span>BREVORA AI</div>
  <h2>Thank You</h2>
  <div class="site"><svg width="20" height="20" viewBox="0 0 20 20" fill="none" stroke="#fff" stroke-width="1.6"><circle cx="10" cy="10" r="8"/><path d="M2 10h16M10 2c3 3 3 13 0 16M10 2c-3 3-3 13 0 16"/></svg>www.brevora.example</div>
  <div class="follow">Follow Us: <i></i><i></i><i></i></div>
</section>

</body>
</html>
```